Dental Practice based in Melbourne needs header designed for mobile website

Verdant Dental Carlow needs logo modified (better color scheme)and the header needs good use of colors (Green should be one of them) . The overall scheme is attached below. Please maintain the overall position of the logo in the center just like the way it is. Icons that should be present : Verdant Dental Carlow, Phone number with phone icon, Menu bar, Book now, search icon, Logo. in the center.

```html
<!DOCTYPE html>
<html lang="en">
<head>
<meta charset="utf-8">
<title>Verdant Dental Carlow</title>
<link rel="stylesheet" href="https://fonts.googleapis.com/css2?family=Roboto:ital,wght@0,400;0,500;0,700;1,700&family=Raleway:wght@400;500;600&family=Kaushan+Script&display=swap">
<style>
:root{
  --blue:#1656c9;
  --blue-dark:#1148b3;
  --blue-light:#3d88ea;
  --green:#4e8f2b;
  --green-bright:#6ba33a;
  --lime:#9bd22d;
  --purple:#8a2f8e;
  --lilac:#8f88cf;
  --ink:#1b1b1b;
  --muted:#5b5b5b;
  --white:#ffffff;
  --grey-bg:#eef0f2;
}
*{margin:0;padding:0;box-sizing:border-box}
html,body{width:1200px;height:4042px;overflow:hidden;background:var(--white)}
body{font-family:'Raleway',sans-serif;color:var(--ink)}
.page{position:relative;width:1200px;height:4042px;overflow:hidden}
.abs{position:absolute}
.heading{font-family:'Roboto',sans-serif;font-weight:700}
.center{text-align:center}

/* top bar */
.topbar{left:0;top:0;width:1200px;height:41px;background:var(--blue)}
.social-sq{position:absolute;top:9px;width:24px;height:24px;border-radius:3px;background:rgba(255,255,255,.85)}
.social-sq.first{top:0;left:77px;width:44px;height:41px;border-radius:0;background:var(--green-bright)}
.social-sq.first::after{content:"";position:absolute;left:11px;top:9px;width:22px;height:22px;border-radius:3px;background:rgba(255,255,255,.85)}
.address-top{right:77px;top:0;height:41px;display:flex;align-items:center;gap:8px;color:var(--white);font-size:14px}

/* header */
.call-icon{left:76px;top:66px}
.call-label{left:143px;top:66px;color:var(--lime);font-size:15px}
.call-number{left:143px;top:88px;color:var(--blue);font-family:'Roboto',sans-serif;font-weight:500;font-size:25px}
.brand{left:0;width:1200px;top:41px;height:105px;display:flex;align-items:center;justify-content:center;gap:14px}
.brand-mark{width:74px;height:74px;border-radius:50%;background:var(--lilac)}
.brand-name{font-family:'Roboto',sans-serif;font-weight:700;font-size:22px;color:var(--purple)}
.book-btn{left:910px;top:67px;width:213px;height:52px;background:var(--blue);display:flex;color:var(--white);font-family:'Roboto',sans-serif;font-size:19px}
.btn-label{flex:1;display:flex;align-items:center;justify-content:center}
.btn-arrow{width:42px;background:var(--green-bright);display:flex;align-items:center;justify-content:center}

/* nav */
.nav{left:0;top:146px;width:1200px;height:63px;background:var(--green)}
.nav-item{position:absolute;top:0;height:63px;display:flex;align-items:center;justify-content:center;color:var(--white);font-family:'Roboto',sans-serif;font-size:15px}
.nav-item.active{background:var(--blue)}

/* hero */
.hero{left:0;top:209px;width:1200px;height:575px;background:linear-gradient(90deg,#f2f2f2 0%,#ececec 35%,#e3e6e4 100%)}
.hero-photo{left:360px;top:209px;width:840px;height:540px;background:linear-gradient(120deg,#e8e3dc 0%,#e9c7ad 35%,#c3d8a5 70%,#a8c98a 100%)}
.hero-title{left:77px;top:346px;font-family:'Kaushan Script',cursive;font-size:46px;color:var(--ink)}
.hero-sub{left:77px;top:408px;font-family:'Roboto',sans-serif;font-weight:700;font-style:italic;font-size:22px}
.hero-text{left:79px;top:456px;width:400px;font-size:14px;line-height:27px;color:#333}
.contact-btn{left:77px;top:522px;width:209px;height:52px;background:var(--blue);display:flex;color:var(--white);font-family:'Roboto',sans-serif;font-size:19px}
.hero-arrow{top:412px;width:52px;height:52px;border-radius:50%;background:rgba(90,90,90,.75);display:flex;align-items:center;justify-content:center}

/* welcome */
.kicker{left:0;width:1200px;font-family:'Roboto',sans-serif;font-weight:500;font-size:19px;color:var(--green)}
.section-title{left:0;width:1200px;font-size:40px;color:var(--blue)}
.welcome-copy{left:240px;top:904px;width:720px;font-size:14px;line-height:27px;color:var(--muted)}
.welcome-copy p{margin-bottom:14px}
.learn-btn{left:496px;top:1173px;width:208px;height:52px;background:var(--blue);display:flex;color:var(--white);font-family:'Roboto',sans-serif;font-size:19px}
.team-photo{left:180px;top:1263px;width:824px;height:294px;background:linear-gradient(180deg,#ffffff 0%,#eef1f5 30%,#dfe5ee 100%);border-radius:140px 140px 0 0}

/* feature tiles */
.tile{position:absolute;top:1557px;width:300px;height:234px;display:flex;flex-direction:column;align-items:center;color:var(--white)}
.tile-icon{margin-top:46px;width:82px;height:82px;border-radius:50%;border:3px solid var(--white);display:flex;align-items:center;justify-content:center}
.tile-icon span{width:64px;height:64px;border-radius:50%;background:var(--white);display:flex;align-items:center;justify-content:center}
.tile-label{margin-top:22px;font-family:'Roboto',sans-serif;font-weight:700;font-size:22px}

/* treatments */
.service{position:absolute;width:104px;height:104px;border-radius:50%;background:var(--green);display:flex;align-items:center;justify-content:center}
.service.implant{background:linear-gradient(90deg,#1c5fd0,#4e8f2b)}
.service-label{position:absolute;font-family:'Roboto',sans-serif;font-weight:500;font-size:15px;line-height:23px;color:var(--ink)}
.service-hub{left:475px;top:2168px;width:250px;height:250px;border-radius:50%;background:var(--lilac)}

/* testimonials */
.reviews{left:0;top:2482px;width:1200px;height:519px;background:linear-gradient(120deg,#2a6ad6 0%,#1656c9 55%,#2c73dc 100%)}
.reviews-title{left:0;top:2536px;width:1200px;font-size:40px;color:var(--white)}
.avatar{left:538px;top:2616px;width:124px;height:124px;border-radius:50%;border:5px solid var(--white);background:linear-gradient(160deg,#e6c3a6,#b98a6a)}
.reviewer{left:0;top:2768px;width:1200px;font-family:'Roboto',sans-serif;font-weight:700;font-size:17px;color:var(--white)}
.stars{left:0;top:2796px;width:1200px;display:flex;justify-content:center;gap:4px}
.review-text{left:240px;top:2852px;width:720px;font-size:14px;line-height:27px;color:var(--white)}

/* partners */
.partner{position:absolute;top:3172px;width:150px;height:50px;border-radius:8px;background:#e6ebf2}

/* booking */
.booking{left:0;top:3313px;width:1200px;height:331px;background:var(--green-bright)}
.booking-photo{left:675px;top:3333px;width:425px;height:311px;border-radius:200px 200px 0 0;background:linear-gradient(180deg,#6b4a35 0%,#d6b39a 40%,#f4f1ee 100%)}
.booking-title{left:212px;top:3398px;font-size:40px;color:var(--white)}
.booking-sub{left:212px;top:3460px;width:340px;font-family:'Roboto',sans-serif;font-size:17px;color:var(--white)}
.field{position:absolute;top:3509px;height:52px;border:1px solid rgba(255,255,255,.85);display:flex;align-items:center;padding-left:18px;font-size:14px;color:var(--white)}
.field.solid{background:var(--white)}
.send-btn{left:623px;top:3509px;width:42px;height:52px;background:var(--blue);display:flex;align-items:center;justify-content:center}

/* footer */
.footer{left:0;top:3644px;width:1200px;height:336px;background:var(--blue)}
.foot-head{position:absolute;top:3684px;font-family:'Roboto',sans-serif;font-weight:700;font-size:17px;color:var(--white)}
.foot-links{left:77px;top:3730px;list-style:none;color:rgba(255,255,255,.9);font-size:14px;line-height:32px}
.foot-links li:first-child{font-weight:600;color:var(--white)}
.foot-quote{left:340px;top:3730px;width:240px;font-size:13px;line-height:25px;color:var(--white)}
.foot-author{left:355px;top:3840px;font-family:'Roboto',sans-serif;font-size:16px;color:var(--white)}
.contact-block{left:640px;top:3731px;font-size:13px;line-height:25px;color:var(--white)}
.contact-block strong{font-family:'Roboto',sans-serif;font-weight:700;font-size:13px}
.foot-social{position:absolute;top:3889px;width:38px;height:38px;border-radius:50%;border:2px solid var(--white);background:rgba(255,255,255,.15)}
.foot-social.first{background:var(--green-bright)}
.map{left:874px;top:3733px;width:249px;height:165px;background:linear-gradient(135deg,#eef0ee 0%,#e2e6e1 60%,#d9dfd6 100%)}
.bottombar{left:0;top:3980px;width:1200px;height:62px;background:var(--green);display:flex;align-items:center;justify-content:center;color:var(--white);font-size:13px}
</style>
</head>
<body>
<div class="page">

  <!-- top bar -->
  <div class="abs topbar">
    <span class="social-sq first"></span>
    <span class="social-sq" style="left:130px"></span>
    <span class="social-sq" style="left:172px"></span>
    <span class="social-sq" style="left:214px"></span>
    <div class="abs address-top">
      <svg width="14" height="20" viewBox="0 0 14 20"><path d="M7 0C3.1 0 0 3.1 0 7c0 5 7 13 7 13s7-8 7-13c0-3.9-3.1-7-7-7z" fill="#9bd22d"/><circle cx="7" cy="7" r="2.6" fill="#1656c9"/></svg>
      14 Fernhill Road Carlow West 3071
    </div>
  </div>

  <!-- header -->
  <svg class="abs call-icon" width="52" height="54" viewBox="0 0 24 24"><path d="M6.6 10.8c1.4 2.8 3.8 5.1 6.6 6.6l2.2-2.2c.3-.3.7-.4 1-.2 1.1.4 2.3.6 3.6.6.6 0 1 .4 1 1V20c0 .6-.4 1-1 1C10.6 21 3 13.4 3 4c0-.6.4-1 1-1h3.5c.6 0 1 .4 1 1 0 1.3.2 2.5.6 3.6.1.3 0 .7-.2 1z" fill="#1656c9"/></svg>
  <div class="abs call-label">Call Us Now :</div>
  <div class="abs call-number">(03) 9555 0142</div>

  <div class="abs brand">
    <span class="brand-mark"></span>
    <span class="brand-name">Verdant Dental Carlow</span>
  </div>

  <div class="abs book-btn"><span class="btn-label">BOOK NOW</span><span class="btn-arrow"><svg width="14" height="26" viewBox="0 0 14 26"><path d="M2 2l10 11L2 24" stroke="#fff" stroke-width="2" fill="none"/></svg></span></div>

  <!-- nav -->
  <nav class="abs nav">
    <div class="nav-item active" style="left:77px;width:226px">HOLISTIC APPROACH</div>
    <div class="nav-item" style="left:303px;width:150px">TREAMENT</div>
    <div class="nav-item" style="left:453px;width:150px">ABOUT US</div>
    <div class="nav-item" style="left:603px;width:330px">COURES ( NORTHBANK COLLABORATION )</div>
    <svg class="abs" style="left:1104px;top:22px" width="20" height="20" viewBox="0 0 20 20"><circle cx="8" cy="8" r="5.5" stroke="#2b2b2b" stroke-width="2.4" fill="none"/><path d="M12 12l5 5" stroke="#2b2b2b" stroke-width="2.6"/></svg>
  </nav>

  <!-- hero -->
  <section class="abs hero"></section>
  <div class="abs hero-photo" role="img" aria-label="Photo of a smiling family of four, parents carrying two children on their backs, outdoors in soft green light"></div>
  <svg class="abs" style="left:0;top:634px" width="1200" height="152" viewBox="0 0 1200 152">
    <defs><linearGradient id="swoosh" x1="0" x2="1"><stop offset="0" stop-color="#4e8f2b"/><stop offset=".6" stop-color="#3f8a3a"/><stop offset="1" stop-color="#1656c9"/></linearGradient></defs>
    <path d="M0 100 C200 160 470 140 690 78 C890 20 1080 40 1200 150 L1200 152 L0 152 Z" fill="#fff"/>
    <path d="M390 138 C640 40 980 -10 1200 120 L1200 150 C1070 40 880 30 690 78 C560 110 470 130 390 138 Z" fill="url(#swoosh)"/>
  </svg>
  <div class="abs hero-title">Creating Vibrant Smile</div>
  <div class="abs hero-sub">For Healthy Lifestyles !</div>
  <p class="abs hero-text">“OUR GUARANTEE” If you are not happy with your first consultation you will get this for free.</p>
  <div class="abs contact-btn"><span class="btn-label">CONTACT US</span><span class="btn-arrow"><svg width="14" height="26" viewBox="0 0 14 26"><path d="M2 2l10 11L2 24" stroke="#fff" stroke-width="2" fill="none"/></svg></span></div>
  <div class="abs hero-arrow" style="left:12px"><svg width="14" height="24" viewBox="0 0 14 24"><path d="M12 2L2 12l10 10" stroke="#fff" stroke-width="2.5" fill="none"/></svg></div>
  <div class="abs hero-arrow" style="left:1135px"><svg width="14" height="24" viewBox="0 0 14 24"><path d="M2 2l10 10L2 22" stroke="#fff" stroke-width="2.5" fill="none"/></svg></div>

  <!-- welcome -->
  <div class="abs kicker center" style="top:804px">WELCOME TO</div>
  <h1 class="abs section-title heading center" style="top:836px">VERDANT DENTAL CARLOW</h1>
  <div class="abs welcome-copy center">
    <p>Verdant Dental Carlow is a leading dental practice for those in the Carlow area of Melbourne but also throughout Victoria. What differentiates us from other practices is that at Verdant Dental Carlow, we truly put our patients first.</p>
    <p>This means providing a comforting and stress free experience so that even the most nervous patient feels relaxed and confident within our practice environment.</p>
    <p>We devise individual treatment plans for our clients using the most suitable and state of the art technology, enabling us to offer a holistic approach to dentistry. Our years of successful experience allows us to get to the root of any dental problem in a pain free environment.</p>
  </div>
  <div class="abs learn-btn"><span class="btn-label">LEARN MORE</span><span class="btn-arrow"><svg width="14" height="26" viewBox="0 0 14 26"><path d="M2 2l10 11L2 24" stroke="#fff" stroke-width="2" fill="none"/></svg></span></div>
  <div class="abs team-photo" role="img" aria-label="Group photo of the seven-member dental team in white coats"></div>

  <!-- tiles -->
  <div class="tile" style="left:0;background:linear-gradient(135deg,#4a92ee,#2f79e0)">
    <div class="tile-icon"><span><svg width="30" height="38" viewBox="0 0 30 38"><path d="M6 11a9 9 0 1 1 13 8c-3 1.6-4 3-4 6" stroke="#1656c9" stroke-width="5" fill="none" stroke-linecap="round"/><circle cx="15" cy="34" r="3.2" fill="#1656c9"/></svg></span></div>
    <div class="tile-label">WHY US ?</div>
  </div>
  <div class="tile" style="left:300px;background:var(--green)">
    <div class="tile-icon"><span><svg width="34" height="34" viewBox="0 0 34 34"><rect x="3" y="6" width="28" height="25" rx="2" stroke="#4e8f2b" stroke-width="3" fill="none"/><path d="M3 13h28M10 2v7M24 2v7" stroke="#4e8f2b" stroke-width="3"/><path d="M9 18h4M15 18h4M21 18h4M9 24h4M15 24h4M21 24h4" stroke="#4e8f2b" stroke-width="3"/></svg></span></div>
    <div class="tile-label">OPENING HOURS</div>
  </div>
  <div class="tile" style="left:600px;background:linear-gradient(135deg,#2a6fe0,#1656c9)">
    <div class="tile-icon"><span><svg width="36" height="30" viewBox="0 0 36 30"><ellipse cx="14" cy="12" rx="13" ry="10" fill="#1656c9"/><path d="M6 19l-3 7 8-4z" fill="#1656c9"/><ellipse cx="24" cy="16" rx="11" ry="8.5" fill="#1656c9" stroke="#fff" stroke-width="2"/></svg></span></div>
    <div class="tile-label">BLOG</div>
  </div>
  <div class="tile" style="left:900px;background:linear-gradient(135deg,#1e63d6,#1349b6)">
    <div class="tile-icon"><span><svg width="24" height="34" viewBox="0 0 14 20"><path d="M7 0C3.1 0 0 3.1 0 7c0 5 7 13 7 13s7-8 7-13c0-3.9-3.1-7-7-7z" fill="#1656c9"/><circle cx="7" cy="7" r="2.6" fill="#fff"/></svg></span></div>
    <div class="tile-label">GET DIRACTION</div>
  </div>

  <!-- treatments -->
  <div class="abs kicker center" style="top:1853px">WHAT WE DO</div>
  <h2 class="abs section-title heading center" style="top:1880px">OUR TREAMENT</h2>
  <svg class="abs" style="left:250px;top:1955px" width="700" height="527" viewBox="0 0 700 527">
    <circle cx="350" cy="351" r="342" stroke="#9aa7c8" stroke-width="1.5" stroke-dasharray="3 5" fill="none"/>
  </svg>
  <div class="abs service-hub" aria-hidden="true"></div>

  <div class="service" style="left:455px;top:2019px"><svg width="56" height="56" viewBox="0 0 56 56" fill="none" stroke="#fff" stroke-width="2.4"><path d="M10 14c0-6 8-6 10-2 2-4 10-4 10 2 0 7-3 10-5 16-1 3-4 3-5 0-1 3-4 3-5 0-2-6-5-9-5-16z" transform="translate(0 2)"/><path d="M26 14c0-6 8-6 10-2 2-4 10-4 10 2 0 7-3 10-5 16-1 3-4 3-5 0-1 3-4 3-5 0-2-6-5-9-5-16z" transform="translate(0 2)"/><path d="M8 22h40M8 40h40"/><rect x="12" y="36" width="8" height="8"/><rect x="36" y="36" width="8" height="8"/></svg></div>
  <div class="service" style="left:648px;top:2019px"><svg width="50" height="56" viewBox="0 0 50 56" fill="none" stroke="#fff" stroke-width="2.6"><path d="M8 10c0-8 12-9 17-4 5-5 17-4 17 4 0 12-5 16-7 34-1 6-6 6-7 0l-3-14-3 14c-1 6-6 6-7 0C13 26 8 22 8 10z"/><path d="M22 20l3 5 3-5" /></svg></div>
  <div class="service" style="left:304px;top:2108px"><svg width="56" height="56" viewBox="0 0 56 56" fill="none" stroke="#fff" stroke-width="2.4"><path d="M22 10c0-6 9-7 13-3 4-4 13-3 13 3 0 9-4 12-5 25-1 4-5 4-6 0l-2-9-2 9c-1 4-5 4-6 0-1-13-5-16-5-25z"/><path d="M10 16v32M6 16h8M10 48h4"/><path d="M6 50h44"/></svg></div>
  <div class="service" style="left:800px;top:2108px"><svg width="56" height="56" viewBox="0 0 56 56" fill="none" stroke="#fff" stroke-width="2.4"><path d="M6 28h44c0 12-10 18-22 18S6 40 6 28z"/><path d="M20 46l-2 6h20l-2-6"/><path d="M30 28l12-18"/><circle cx="16" cy="18" r="5"/></svg></div>
  <div class="service implant" style="left:224px;top:2254px"><svg width="44" height="56" viewBox="0 0 44 56" fill="none" stroke="#fff" stroke-width="2.6"><path d="M6 10c0-7 10-8 16-3 6-5 16-4 16 3 0 6-3 9-4 12H10C9 19 6 16 6 10z"/><path d="M12 26h20M13 32h18M15 38h14M17 44h10M19 50h6"/></svg></div>
  <div class="service" style="left:880px;top:2254px"><svg width="56" height="56" viewBox="0 0 56 56" fill="none" stroke="#fff" stroke-width="2.4"><path d="M12 34h30l6-10"/><path d="M16 34v-8c0-4 3-6 6-6h8"/><path d="M26 34v12M16 50h22"/><circle cx="36" cy="10" r="5"/><path d="M36 15v8"/></svg></div>

  <div class="service-label center" style="left:367px;top:1960px;width:200px">CHILDREN/TEENS/<br>ADULTS BRACES</div>
  <div class="service-label" style="left:673px;top:1960px;width:200px;line-height:17px">SNORING/<br>GRINDING TMJ</div>
  <div class="service-label" style="left:134px;top:2130px;width:150px;text-align:right">GENERAL<br>DENTISTRY</div>
  <div class="service-label" style="left:930px;top:2118px;width:150px">COSMETIC<br>DENTISTRY</div>
  <div class="service-label" style="left:59px;top:2289px;width:150px;text-align:right">IMPLANTS</div>

  <!-- testimonials -->
  <section class="abs reviews" role="img" aria-label="Softly faded photo of a dental check-up behind the blue tint"></section>
  <h2 class="abs reviews-title heading center">WHAT PATIENTS ARE SAYING ABOUT US</h2>
  <svg class="abs" style="left:498px;top:2664px" width="18" height="28" viewBox="0 0 18 28"><path d="M14 2L4 14l10 12" stroke="rgba(255,255,255,.7)" stroke-width="2.2" fill="none"/></svg>
  <svg class="abs" style="left:684px;top:2664px" width="18" height="28" viewBox="0 0 18 28"><path d="M4 2l10 12L4 26" stroke="rgba(255,255,255,.7)" stroke-width="2.2" fill="none"/></svg>
  <div class="abs avatar" role="img" aria-label="Portrait photo of the reviewing patient"></div>
  <div class="abs reviewer center">PRIYA</div>
  <div class="abs stars">
    <svg width="24" height="23" viewBox="0 0 24 23"><path d="M12 0l3.5 7.6 8.3.9-6.2 5.6 1.8 8.2L12 18l-7.4 4.3 1.8-8.2L.2 8.5l8.3-.9z" fill="#f5c518"/></svg>
    <svg width="24" height="23" viewBox="0 0 24 23"><path d="M12 0l3.5 7.6 8.3.9-6.2 5.6 1.8 8.2L12 18l-7.4 4.3 1.8-8.2L.2 8.5l8.3-.9z" fill="#f5c518"/></svg>
    <svg width="24" height="23" viewBox="0 0 24 23"><path d="M12 0l3.5 7.6 8.3.9-6.2 5.6 1.8 8.2L12 18l-7.4 4.3 1.8-8.2L.2 8.5l8.3-.9z" fill="#f5c518"/></svg>
    <svg width="24" height="23" viewBox="0 0 24 23"><path d="M12 0l3.5 7.6 8.3.9-6.2 5.6 1.8 8.2L12 18l-7.4 4.3 1.8-8.2L.2 8.5l8.3-.9z" fill="#f5c518"/></svg>
    <svg width="24" height="23" viewBox="0 0 24 23"><path d="M12 0l3.5 7.6 8.3.9-6.2 5.6 1.8 8.2L12 18l-7.4 4.3 1.8-8.2L.2 8.5l8.3-.9z" fill="#f5c518"/></svg>
  </div>
  <p class="abs review-text center">* Cant speak highly enough about this practice. All staff are proffessional, and all treatment/work is done to a very high standard. Customer service is also brilliant! Wouldnt go anywhere else. Make sure you request Rosa for your nurse she is a solid *</p>

  <!-- partners -->
  <h2 class="abs section-title heading center" style="top:3060px">OUR PARTNERS / SPONSORS</h2>
  <div class="partner" style="left:124px"></div>
  <div class="partner" style="left:344px"></div>
  <div class="partner" style="left:549px"></div>
  <div class="partner" style="left:753px"></div>
  <div class="partner" style="left:951px"></div>

  <!-- booking -->
  <section class="abs booking"></section>
  <svg class="abs" style="left:540px;top:3400px" width="460" height="150" viewBox="0 0 460 150"><path d="M10 20 C120 -10 260 0 330 60 C370 95 400 120 440 140" stroke="rgba(255,255,255,.8)" stroke-width="1.5" stroke-dasharray="6 5" fill="none"/></svg>
  <div class="abs booking-photo" role="img" aria-label="Photo of a smiling woman making an OK gesture"></div>
  <h2 class="abs booking-title heading">ONLINE BOOKING</h2>
  <svg class="abs" style="left:548px;top:3407px" width="26" height="22" viewBox="0 0 26 22"><path d="M1 11L25 1 19 21 12 14z M12 14l13-13" stroke="#fff" stroke-width="1.6" fill="none"/></svg>
  <div class="abs booking-sub center">Provide 24/7 services</div>
  <div class="field" style="left:105px;width:345px">Enter Your Email *</div>
  <div class="field solid" style="left:456px;width:167px"></div>
  <div class="abs send-btn"><svg width="14" height="26" viewBox="0 0 14 26"><path d="M2 2l10 11L2 24" stroke="#fff" stroke-width="2" fill="none"/></svg></div>

  <!-- footer -->
  <footer class="abs footer"></footer>
  <div class="foot-head" style="left:75px">SITEMAP</div>
  <div class="foot-head" style="left:340px">TESTIMONIALS</div>
  <div class="foot-head" style="left:606px">GET IN TOUCH</div>
  <div class="foot-head" style="left:875px">LOCATION MAP</div>

  <ul class="abs foot-links">
    <li>» Home</li>
    <li>» Holistic Approacj</li>
    <li>» Treament</li>
    <li>» About Us</li>
    <li>» Coures( Northbank Collaboration)</li>
  </ul>

  <p class="abs foot-quote">“ Great and friendly staff the nurse max took great care of me as well as doctor Henry. Couldn't have asked for better service ”</p>
  <div class="abs foot-author">— Liam Ferris</div>
  <svg class="abs" style="left:358px;top:3880px" width="36" height="22" viewBox="0 0 36 22"><path d="M10 2L3 11l7 9M26 2l7 9-7 9" stroke="#fff" stroke-width="2" fill="none"/></svg>

  <svg class="abs" style="left:606px;top:3735px" width="20" height="26" viewBox="0 0 20 26"><path d="M10 0v26M3 5h14l2 3-2 3H3zM17 14H3l-2 3 2 3h14" fill="#fff"/></svg>
  <div class="abs contact-block">
    <strong>VERDANT DENTAL CARLOW</strong><br>
    14 Fernhill Road<br>
    Carlow West 3071<br>
    Get Directin
  </div>
  <svg class="abs" style="left:606px;top:3846px" width="20" height="20" viewBox="0 0 24 24"><path d="M6.6 10.8c1.4 2.8 3.8 5.1 6.6 6.6l2.2-2.2c.3-.3.7-.4 1-.2 1.1.4 2.3.6 3.6.6.6 0 1 .4 1 1V20c0 .6-.4 1-1 1C10.6 21 3 13.4 3 4c0-.6.4-1 1-1h3.5c.6 0 1 .4 1 1 0 1.3.2 2.5.6 3.6.1.3 0 .7-.2 1z" fill="#fff"/></svg>
  <div class="abs" style="left:640px;top:3845px;font-size:13px;color:#fff">(03) 9555 0142</div>
  <span class="foot-social first" style="left:608px"></span>
  <span class="foot-social" style="left:657px"></span>
  <span class="foot-social" style="left:704px"></span>
  <span class="foot-social" style="left:750px"></span>

  <div class="abs map" role="img" aria-label="Street map showing the clinic location in Carlow West"></div>

  <div class="abs bottombar">©VERDANT DENTAL CARLOW - 2019 All Rights Reserved.</div>

</div>
</body>
</html>
```